Nine Moons Rollup Banner/Poster

I provide a Personalised Baby Planning and Maternity Concierge service and I will have a couple of Trade Fair events this year for which I'd like to have a roll-up banner/poster designed. In a nutshell, Nine Moons is a Baby Planning service that helps busy moms and dads by providing guidance, support and education to them in a tailored and unbiased manner. Think of us as a personal assistant in all things pregnancy-related. The company colour schemes can be found on our website at http://www.ninemoons.com.sg - I also have business cards and brochures and can share these designs with you so you get the idea.
--------------------------------------------------------------
TEXT to be on the poster:

The arrival of a new baby can be both exciting and stressful. Let us guide you in making the decisions that are best for your family.

Nine Moons is a Baby Planning service that helps busy moms and dads by providing guidance, support and education to them in a tailored and unbiased manner. Think of us as your personal assistant in all things pregnancy-related. Enjoy your pregnancy journey and make well-informed decisions with confidence, but without the stress!

www.ninemoons.com.sg

An idea would be to have a picture of a mom (of Asian origin) with some thought bubbles containing text like:
- Baby names?
- Birth planning?
- Childbirth classes?
- Baby products?
- Childcare options?
- Full month planning?

Hope it doesn't get too crowded - if it does, we can discuss some changes!

Regards,
Lorena
www.ninemoons.com.sg
Updates

Hi all, Thanks for the first few designs. I think perhaps all that text might be too crowded. Perhaps better to propose design only with the following text: -------------------- The arrival of a new baby can be both exciting and stressful. Let us guide you in making the decisions that are best for your family. www.ninemoons.com.sg -------------------- The thought bubbles can remain - I like them! :-)

Hi as another note - I noticed everyone submitted designs only using the TEAL colour. There's also a small touch of pink on my website.... could you incorporate that in the design in a subtle way somewhere please? That would be nice :-)

Target Market(s)

My target market are pregnant moms! Especially first-time moms.

Industry/Entity Type

Education

Requirements
Must have
• The poster size must be 200cm tall x 85cm wide. There needs to be some margin or bleed area of course. The resolution needs to be a minimum of 300 dpi at actual size.

Please keep to the Nine Moons colour scheme provided in the attached images (business card and brochures).

```html
<!DOCTYPE html>
<html lang="en">
<head>
<meta charset="utf-8">
<title>Nine Moons Roll-up Banner</title>
<link rel="stylesheet" href="https://fonts.googleapis.com/css2?family=Crimson+Text:wght@400;600&family=Josefin+Sans:wght@400&family=Open+Sans:wght@400&display=swap">
<style>
  :root {
    --teal: #66c8cc;
    --ink: #1e1e1e;
    --white: #ffffff;
    --bubble-text: #555555;
    --photo-light: #f7f7f6;
    --photo-mid: #ecebea;
    --photo-warm: #e7ded5;
    --page: #ffffff;
  }
  * { margin: 0; padding: 0; box-sizing: border-box; }
  html, body {
    width: 1200px; height: 1000px; overflow: hidden;
    background: var(--page);
  }
  .canvas { position: relative; width: 1200px; height: 1000px; }
  .banner {
    position: absolute; left: 412px; top: 57px;
    width: 376px; height: 886px;
    background: var(--teal);
    overflow: hidden;
  }
  .brand-band {
    position: absolute; left: 0; top: 0; width: 100%; height: 100px;
    display: flex; align-items: center; justify-content: center;
  }
  .brand-name {
    font-family: "Crimson Text", Georgia, serif;
    font-weight: 600; font-size: 46px; color: var(--ink);
    letter-spacing: 0.5px;
  }
  .hero-photo {
    position: absolute; left: 0; top: 100px; width: 100%; height: 278px;
    background: radial-gradient(ellipse 32% 60% at 48% 62%, var(--photo-warm) 0%, var(--photo-mid) 55%, var(--photo-light) 100%);
  }
  .thought-bubbles {
    position: absolute; left: 0; top: 0; width: 376px; height: 300px;
  }
  .thought-bubbles ellipse, .thought-bubbles circle {
    fill: var(--white); stroke: var(--teal); stroke-width: 2;
  }
  .thought-bubbles text {
    font-family: "Open Sans", Arial, sans-serif;
    font-size: 9px; fill: var(--bubble-text); text-anchor: middle;
  }
  .headline {
    position: absolute; left: 0; top: 390px; width: 100%;
    text-align: center;
    font-family: "Josefin Sans", "Century Gothic", sans-serif;
    font-size: 21px; line-height: 29px; color: var(--white);
  }
  .description {
    position: absolute; left: 18px; top: 541px; width: 350px;
    font-family: "Crimson Text", Georgia, serif;
    font-size: 17.5px; line-height: 26.5px; color: var(--ink);
    white-space: nowrap;
  }
  .web-strip {
    position: absolute; left: 0; top: 793px; width: 100%; height: 47px;
    background: var(--white);
    display: flex; align-items: center; justify-content: center;
    font-family: "Crimson Text", Georgia, serif;
    font-size: 29px; color: var(--ink);
  }
</style>
</head>
<body>
<div class="canvas">
  <div class="banner">
    <div class="brand-band"><span class="brand-name">Nine Moons</span></div>

    <div class="hero-photo" role="img" aria-label="Photo of a smiling pregnant Asian woman in a white dress, looking down at her belly, on a soft white background"></div>

    <svg class="thought-bubbles" viewBox="0 0 376 300" aria-hidden="false">
      <g class="bubble">
        <ellipse cx="160" cy="135" rx="27" ry="21"/>
        <circle cx="190" cy="151" r="3"/><circle cx="197" cy="157" r="2"/>
        <text x="160" y="132">Birth</text><text x="160" y="143">planning?</text>
      </g>
      <g class="bubble">
        <ellipse cx="214" cy="106" rx="28" ry="24"/>
        <circle cx="220" cy="138" r="3"/><circle cx="222" cy="146" r="2"/>
        <text x="214" y="103">Childbirth</text><text x="214" y="114">classes?</text>
      </g>
      <g class="bubble">
        <ellipse cx="278" cy="106" rx="28" ry="27"/>
        <circle cx="268" cy="142" r="3"/><circle cx="264" cy="150" r="2"/>
        <text x="278" y="103">Baby</text><text x="278" y="114">products?</text>
      </g>
      <g class="bubble">
        <ellipse cx="338" cy="130" rx="28" ry="23"/>
        <circle cx="305" cy="150" r="3"/><circle cx="298" cy="155" r="2"/>
        <text x="338" y="127">Childcare</text><text x="338" y="138">options?</text>
      </g>
      <g class="bubble">
        <ellipse cx="345" cy="183" rx="29" ry="27"/>
        <circle cx="311" cy="176" r="3"/><circle cx="303" cy="177" r="2"/>
        <text x="345" y="174">Full</text><text x="345" y="185">month</text><text x="345" y="196">planning?</text>
      </g>
      <g class="bubble">
        <ellipse cx="157" cy="189" rx="25" ry="22"/>
        <circle cx="189" cy="181" r="3"/><circle cx="197" cy="178" r="2"/>
        <text x="157" y="186">Baby</text><text x="157" y="197">names?</text>
      </g>
    </svg>

    <p class="headline">The arrival of a new baby can be<br>both exciting and stressful.<br>Let us guide you in making the<br>decisions that are best for your<br>family.</p>

    <p class="description">Nine Moons is a Baby Planning service that<br>helps busy moms and dads by providing<br>guidance, support and education to them<br>in a tailored and unbiased manner. Think<br>of us as your personal assistant in all things<br>pregnancy-related. Enjoy your pregnancy<br>journey and make well-informed decisions<br>with confidence, but without the stress!</p>

    <div class="web-strip">www.ninemoons.com.sg</div>
  </div>
</div>
</body>
</html>
```